Extra job from Miami Logo design job

This posting is for the winner of the Tessaly Lane Shop logo, we need an example of what the commerce webpage would look like.

Please go here to submit the logo first:

http://jobs.brightpitchworks.com/job.aspx?id=518204.

```html
<!DOCTYPE html>
<html lang="en">
<head>
<meta charset="utf-8">
<title>Tessaly Lane Shop</title>
<link rel="stylesheet" href="https://fonts.googleapis.com/css2?family=Oswald:wght@400;500&family=Open+Sans:ital,wght@0,400;0,600;1,400&display=swap">
<style>
:root{
  --blue:#3bb0e6;
  --blue-dark:#2a9bd3;
  --blue-overlay:rgba(72,182,236,.85);
  --page:#f2f3f7;
  --ink:#2e2e2e;
  --muted:#555;
  --rule:#9a9a9a;
  --red:#e8574a;
  --orange:#f8a532;
  --sky:#21b7ee;
  --navy:#1591d0;
  --charcoal:#3b3b3b;
  --footer:#e6f2f8;
  --pink:#d8427a;
}
*{box-sizing:border-box;margin:0;padding:0}
html,body{width:1200px;height:2326px;overflow:hidden}
body{background:var(--page);font-family:"Open Sans",Arial,sans-serif;color:var(--ink);position:relative}
.abs{position:absolute}

.top-strip{left:0;top:0;width:1200px;height:6px;background:var(--blue)}
.brand{left:0;top:6px;width:1200px;height:124px;display:flex;align-items:center;justify-content:center;gap:16px}
.brand-dot{width:44px;height:44px;border-radius:50%;background:var(--blue)}
.brand-name{font-family:"Open Sans",Arial,sans-serif;font-weight:600;font-size:33px;color:#222}

.nav{left:0;top:130px;width:1200px;height:68px;background:var(--blue)}
.nav::before,.nav::after{content:"";position:absolute;left:0;right:0;border-top:1px dashed rgba(255,255,255,.7)}
.nav::before{top:5px}.nav::after{bottom:5px}
.nav a,.nav span{position:absolute;top:50%;transform:translate(-50%,-50%);color:#fff;font-size:14px;font-weight:600;text-decoration:none;white-space:nowrap}
.nav span{font-size:16px;font-style:italic}

.hero{left:0;top:198px;width:1200px;height:453px;background:radial-gradient(ellipse at 50% 55%,#d9d6d2 0%,#a9a39d 28%,#2b2a2a 55%,#141414 100%)}
.hero-arrow{top:388px;width:44px;height:44px;background:var(--blue);transform:rotate(45deg)}
.hero-arrow svg{transform:rotate(-45deg);width:44px;height:44px}
.dots{top:622px;left:582px;display:flex;gap:6px}
.dots i{width:11px;height:11px;border-radius:50%;border:1.5px solid #fff;display:block}
.dots i.on{background:var(--blue)}

.welcome-title{left:105px;top:683px;width:118px;font-family:"Oswald",sans-serif;font-weight:500;font-size:28px;line-height:38px;color:var(--blue);letter-spacing:-.3px;white-space:nowrap}
.welcome-text{left:236px;top:689px;width:700px;font-size:12px;line-height:18px;color:var(--muted)}
.btn{left:947px;top:685px;width:152px;height:34px;background:var(--blue);color:#fff;font-size:13px;display:flex;align-items:center;justify-content:center;border-radius:2px}

.section-title{left:0;width:1200px;text-align:center;font-family:"Oswald",sans-serif;font-size:24px;font-weight:500;color:#222}
.section-title::before,.section-title::after{content:"";position:absolute;top:50%;width:80px;border-top:1px solid var(--rule)}
.section-title::before{left:450px}.section-title::after{left:670px}

.card{width:244px;height:368px;overflow:hidden;background:#ccc}
.card.active{border:2px solid var(--blue)}
.card .photo{position:absolute;inset:0}
.price-tag{position:absolute;right:0;bottom:0;width:98px;height:43px;background:var(--blue);color:#fff;font-size:13px;font-weight:600;display:flex;align-items:center;justify-content:center}
.overlay{position:absolute;left:0;right:0;bottom:0;height:124px;background:var(--blue-overlay);color:#fff}
.overlay h3{position:absolute;top:14px;width:100%;text-align:center;font-family:"Oswald",sans-serif;font-weight:500;font-size:20px}
.overlay .stars{position:absolute;top:50px;width:100%;text-align:center;font-size:14px;letter-spacing:1px}
.overlay .price{position:absolute;left:16px;bottom:14px;font-size:13px;font-weight:600}
.overlay .tool{position:absolute;bottom:10px;width:28px;height:28px;border:1px solid rgba(255,255,255,.6);display:flex;align-items:center;justify-content:center}

.promo{height:141px;overflow:hidden}
.promo .txt{position:absolute;color:#fff;font-family:"Open Sans",sans-serif;white-space:nowrap}

.feature{top:1873px;width:144px;height:143px;color:#fff;text-align:center}
.feature svg{position:absolute;top:24px;left:50%;transform:translateX(-50%)}
.feature h4{position:absolute;top:74px;width:100%;font-size:14px;font-weight:600}
.feature p{position:absolute;top:96px;left:8px;right:8px;font-size:11px;line-height:14px}

.footer{left:0;top:2047px;width:1200px;height:279px;background:var(--footer)}
.footer-grass{left:0;top:2250px;width:1200px;height:76px;background:linear-gradient(180deg,rgba(180,220,140,0) 0%,#bfe29a 55%,#a9d67f 100%)}
.col{top:2074px}
.col h5{font-size:15px;font-weight:400;color:#333;margin-bottom:14px;letter-spacing:.3px}
.col li{list-style:none;font-size:11.5px;color:#555;line-height:24px}
.phone-line{font-size:13px;color:#444;line-height:23px}
.callout{font-size:11px;color:var(--pink);line-height:17px}
.copyright{left:0;top:2291px;width:1200px;text-align:center;font-size:11px;color:#333}
</style>
</head>
<body>

<div class="abs top-strip"></div>
<header class="abs brand">
  <span class="brand-dot"></span>
  <span class="brand-name">Tessaly Lane Shop</span>
</header>

<nav class="abs nav">
  <a style="left:171px">Home</a><span style="left:256px">//</span>
  <a style="left:338px">About Us</a><span style="left:426px">//</span>
  <a style="left:515px">Products</a><span style="left:598px">//</span>
  <a style="left:679px">Shop</a><span style="left:750px">//</span>
  <a style="left:829px">Blog</a><span style="left:908px">//</span>
  <a style="left:998px">Contact Us</a>
</nav>

<section class="abs hero" role="img" aria-label="Slider photo of a bride in a white gown on a dark damask background"></section>
<div class="abs hero-arrow" style="left:40px"><svg viewBox="0 0 44 44"><path d="M25 14 L17 22 L25 30" fill="none" stroke="#fff" stroke-width="3"/></svg></div>
<div class="abs hero-arrow" style="left:1127px"><svg viewBox="0 0 44 44"><path d="M19 14 L27 22 L19 30" fill="none" stroke="#fff" stroke-width="3"/></svg></div>
<div class="abs dots"><i class="on"></i><i></i><i></i></div>

<h2 class="abs welcome-title">WELCOME!</h2>
<p class="abs welcome-text">Lorem ipsum dolor sit amet, consectetur adipiscing elit integer euismod blandit feugiat proin ut tortor nec Morbi felis ligula pulvinar ullamcorper fermentum adipiscing donec ac molestie metus.</p>
<a class="abs btn">learn More</a>

<h2 class="abs section-title" style="top:764px">NEW ITEMS</h2>

<div class="abs card active" style="left:101px;top:829px">
  <div class="photo" role="img" aria-label="Model wearing a black lace bra top" style="background:linear-gradient(180deg,#f1f1f1,#d9cfc8)"></div>
  <div class="overlay"><h3>WHITE DRESS</h3><div class="stars">★★★★★</div><span class="price">$250.00</span>
    <span class="tool" style="right:52px"><svg width="16" height="14" viewBox="0 0 16 14"><path d="M1 1h3l2 8h8l1-6H5" fill="none" stroke="#fff" stroke-width="1.3"/><circle cx="7" cy="12" r="1.2" fill="#fff"/><circle cx="13" cy="12" r="1.2" fill="#fff"/></svg></span>
    <span class="tool" style="right:10px"><svg width="14" height="14" viewBox="0 0 14 14"><path d="M6 8 L8 6 M5 6 L3 8 a2 2 0 0 0 3 3 l2-2 M9 8 l2-2 a2 2 0 0 0-3-3 L6 5" fill="none" stroke="#fff" stroke-width="1.3"/></svg></span>
  </div>
</div>
<div class="abs card" style="left:352px;top:829px">
  <div class="photo" role="img" aria-label="Model in a pink bikini, grey backdrop" style="background:linear-gradient(180deg,#cfcfcf,#c4c4c4)"></div>
  <span class="price-tag">$250.00</span>
</div>
<div class="abs card" style="left:603px;top:829px">
  <div class="photo" role="img" aria-label="Model in a white bikini on a beach" style="background:linear-gradient(180deg,#bcd9ee 0%,#8fc6df 45%,#e9e2d6 100%)"></div>
  <span class="price-tag">$250.00</span>
</div>
<div class="abs card" style="left:854px;top:829px">
  <div class="photo" role="img" aria-label="Model in a purple bikini, grey backdrop" style="background:linear-gradient(180deg,#cdcdcd,#c2c2c2)"></div>
  <span class="price-tag">$250.00</span>
</div>

<h2 class="abs section-title" style="top:1226px">SALE ITEMS</h2>

<div class="abs card active" style="left:101px;top:1291px">
  <div class="photo" role="img" aria-label="Model in a pink bandeau bikini" style="background:linear-gradient(180deg,#f4f4f4,#e6d6d2)"></div>
  <div class="overlay"><h3>WHITE DRESS</h3><div class="stars">★★★★★</div><span class="price">$250.00</span>
    <span class="tool" style="right:52px"><svg width="16" height="14" viewBox="0 0 16 14"><path d="M1 1h3l2 8h8l1-6H5" fill="none" stroke="#fff" stroke-width="1.3"/><circle cx="7" cy="12" r="1.2" fill="#fff"/><circle cx="13" cy="12" r="1.2" fill="#fff"/></svg></span>
    <span class="tool" style="right:10px"><svg width="14" height="14" viewBox="0 0 14 14"><path d="M6 8 L8 6 M5 6 L3 8 a2 2 0 0 0 3 3 l2-2 M9 8 l2-2 a2 2 0 0 0-3-3 L6 5" fill="none" stroke="#fff" stroke-width="1.3"/></svg></span>
  </div>
</div>
<div class="abs card" style="left:352px;top:1291px">
  <div class="photo" role="img" aria-label="Model in a plaid bikini outdoors among trees" style="background:linear-gradient(180deg,#4f6a3e,#9aa07f 60%,#c9a79a)"></div>
  <span class="price-tag">$250.00</span>
</div>
<div class="abs card" style="left:603px;top:1291px">
  <div class="photo" role="img" aria-label="Model in a red bikini, grey backdrop" style="background:linear-gradient(180deg,#8d8d8d,#b1b1b1)"></div>
  <span class="price-tag">$250.00</span>
</div>
<div class="abs card" style="left:854px;top:1291px">
  <div class="photo" role="img" aria-label="Model in a white embroidered beach cover-up" style="background:linear-gradient(180deg,#f6f6f6,#ececec)"></div>
  <span class="price-tag">$250.00</span>
</div>

<div class="abs promo" style="left:101px;top:1701px;width:318px" role="img" aria-label="Red quilted handbag promotion">
  <div class="abs" style="inset:0;background:linear-gradient(90deg,#5b4036,#3f302b)"></div>
  <span class="txt" style="right:18px;top:10px;font-size:24px">SPECIAL OFFER</span>
  <span class="txt" style="right:18px;top:34px;font-size:42px;color:var(--red)">30%</span>
</div>
<div class="abs promo" style="left:440px;top:1701px;width:318px" role="img" aria-label="Woman in a red sun hat">
  <div class="abs" style="inset:0;background:linear-gradient(90deg,#6e6a66,#8c7a6c 60%,#4b3a33)"></div>
  <span class="txt" style="left:15px;top:82px;font-size:21px">LOREM DOLOR</span>
  <span class="txt" style="left:15px;top:110px;font-size:15px">Proin eget sapien eu enim varius</span>
</div>
<div class="abs promo" style="left:780px;top:1701px;width:318px" role="img" aria-label="Blonde model portrait">
  <div class="abs" style="inset:0;background:linear-gradient(90deg,#4a4a4a 0%,#5c5c5c 55%,#c9b79c 100%)"></div>
  <span class="txt" style="left:17px;top:14px;font-size:27px">DONEC</span>
  <span class="txt" style="left:17px;top:54px;font-size:13px;font-style:italic;line-height:17px">Lorem psum dolor aet<br>dignissim nunc .</span>
</div>

<div class="abs feature" style="left:101px;background:#1ea6e6">
  <svg width="36" height="36" viewBox="0 0 24 24"><path d="M2 10h4v12H2zM8 21V10l5-8c2 0 3 1 2 4l-1 3h6c1 0 2 1 2 2l-2 8c0 1-1 2-2 2z" fill="#fff"/></svg>
  <h4>GUARANTEE</h4><p>100% Money Back Guarantee*</p>
</div>
<div class="abs feature" style="left:271px;background:var(--red)">
  <svg width="36" height="36" viewBox="0 0 24 24"><path d="M2 2h9l11 11-9 9L2 11z" fill="#fff"/><circle cx="7" cy="7" r="2" fill="#e8574a"/></svg>
  <h4>AFFORDABLE</h4><p>Convenient &amp; affordable prices for you</p>
</div>
<div class="abs feature" style="left:441px;background:var(--orange)">
  <svg width="36" height="36" viewBox="0 0 24 24"><path d="M3 15v-3a9 9 0 0 1 18 0v3" fill="none" stroke="#fff" stroke-width="2.4"/><rect x="2" y="14" width="5" height="8" rx="1" fill="#fff"/><rect x="17" y="14" width="5" height="8" rx="1" fill="#fff"/></svg>
  <h4>24/7 SUPPORT</h4><p>We support everything we sell</p>
</div>
<div class="abs feature" style="left:612px;background:var(--sky)">
  <svg width="36" height="36" viewBox="0 0 24 24"><circle cx="12" cy="4" r="2.5" fill="#fff"/><path d="M8 8h8l-1 7h-1v8h-4v-8H9z" fill="#fff"/></svg>
  <h4>SUMMER SALE</h4><p>Upto 50% off on all women wear</p>
</div>
<div class="abs feature" style="left:783px;background:var(--navy)">
  <svg width="36" height="36" viewBox="0 0 24 24"><rect x="3" y="9" width="18" height="4" fill="#fff"/><rect x="4" y="13" width="16" height="9" fill="#fff"/><rect x="11" y="9" width="2" height="13" fill="#1591d0"/><path d="M12 9C9 3 5 5 8 9M12 9c3-6 7-4 4 0" fill="none" stroke="#fff" stroke-width="1.8"/></svg>
  <h4>SURPRISE GIFT</h4><p>Value $50 on orders over $700</p>
</div>
<div class="abs feature" style="left:955px;background:var(--charcoal)">
  <svg width="38" height="36" viewBox="0 0 26 24"><rect x="1" y="5" width="15" height="12" fill="#fff"/><path d="M16 9h5l4 4v4h-9z" fill="#fff"/><circle cx="6" cy="19" r="2.5" fill="#fff"/><circle cx="20" cy="19" r="2.5" fill="#fff"/></svg>
  <h4>FREE SHIPPING</h4><p>All over in world over $100</p>
</div>

<footer class="abs footer"></footer>
<div class="abs footer-grass" role="img" aria-label="Illustrated grass and flowers along the footer edge"></div>

<div class="abs col" style="left:101px">
  <h5>SUPPORT</h5>
  <div style="display:flex;gap:12px;align-items:center">
    <svg width="26" height="26" viewBox="0 0 26 26"><circle cx="13" cy="13" r="12" fill="none" stroke="var(--pink)" stroke-width="1.5"/><path d="M9 7l3 3-2 2c1 2 2 3 4 4l2-2 3 3-2 2c-5 0-10-5-10-10z" fill="var(--pink)"/></svg>
    <div class="phone-line">(+01) 0555 214 386<br>(+84) 0555 214 372</div>
  </div>
  <div class="callout" style="margin-top:12px">WE'RE AVAILABLE 24/7,<br>DON'T HESITATE TO CALL US</div>
</div>
<div class="abs col" style="left:341px">
  <h5>INFORMATION</h5>
  <ul><li>Specials</li><li>New products</li><li>Best sellers</li><li>Our stores</li><li>Contact us</li><li>Sitemap</li></ul>
</div>
<div class="abs col" style="left:522px">
  <h5>CUSTOMER SERVICE</h5>
  <ul><li>Delivery</li><li>Legal Notice</li><li>Terms and conditions of use</li><li>About us</li><li>Secure payment</li></ul>
</div>
<div class="abs col" style="left:744px">
  <h5>MY ACCOUNT</h5>
  <ul><li>My orders</li><li>My credit slips</li><li>My addresses</li><li>My personal info</li><li>My vouchers</li><li>Sign out</li></ul>
</div>
<div class="abs col" style="left:944px">
  <h5>EXTRAS</h5>
  <ul><li>Brands</li><li>Gift Vouchers</li><li>Affiliates</li><li>Specials</li></ul>
</div>

<p class="abs copyright">© 2014 Tessaly Lane Shop All Rights Reserved.</p>

</body>
</html>
```